Lorn's Cleaners new delivery postcard

We need to advertise for our new pick up and delivery dry cleaning/laundry service.
Mens Business Shirts $2.00
Pants $4.50
Skirts $5.00
Dry Clean Shirt/Blouse $5.00
Dress $9.00
2 Piece Suits $9.00
Updates
We would like to use a 5x7 size postcard, printed on both sides. We would like to add a discount to the card for 25% off of their first order, with the flyer.
We are a famly run dry cleaners. My name is Lorn's Cleaners and my cell # is 614-372-0481. We are trying to expand our business to include free pick and delivery.
If possible can you use the logo I sent some where on the postcard? The phone # for the store is 614-205-3967.
Reason: Still need to get partners approval.
Industry/Entity Type
Business

```html
<!DOCTYPE html>
<html lang="en">
<head>
<meta charset="utf-8">
<title>Lorn's Cleaners – Delivery Postcard</title>
<link rel="stylesheet" href="https://fonts.googleapis.com/css2?family=Hind:wght@300;400;500;600;700&family=Open+Sans:ital,wght@1,800&display=swap">
<style>
  :root {
    --backdrop: #6b6669;
    --navy: #0d4a8e;
    --teal: #1a9bbf;
    --teal-text: #2aa3c4;
    --ink: #222;
    --grey-text: #666;
    --white: #fff;
  }
  * { margin: 0; padding: 0; box-sizing: border-box; }
  html, body { width: 1200px; height: 900px; overflow: hidden; }
  body {
    background: var(--backdrop);
    font-family: "Hind", "Helvetica Neue", Arial, sans-serif;
    position: relative;
  }
  .card {
    position: absolute;
    background: var(--white);
    overflow: hidden;
    box-shadow: 0 14px 22px rgba(0,0,0,.35);
  }
  .card-front { left: 44px; top: 66px; width: 544px; height: 762px; }
  .card-back  { left: 613px; top: 66px; width: 544px; height: 760px; }

  .photo { position: absolute; left: 0; width: 100%; }
  .photo-laundry {
    top: 0; height: 379px;
    background:
      radial-gradient(ellipse 260px 240px at 62% 42%, #2b6cc0 0%, #3a78c4 35%, rgba(150,178,214,.6) 65%, rgba(233,235,238,0) 100%),
      linear-gradient(90deg, #dfe2e6 0%, #eef0f2 40%, #e6e8eb 100%);
  }
  .photo-shirts {
    top: 389px; height: 280px;
    background: linear-gradient(120deg, #cfd6e2 0%, #e8b9b9 35%, #f0c5c3 50%, #c9d3e3 75%, #e8e3da 100%);
  }
  .photo-ironing {
    top: 0; height: 277px;
    background: linear-gradient(100deg, #b9c8e8 0%, #f1f1f4 35%, #ecd8dc 65%, #c9c3e6 100%);
  }

  .offer-ring {
    position: absolute; left: 146px; top: 251px;
    width: 256px; height: 256px; border-radius: 50%;
    border: 2px solid var(--white);
  }
  .offer {
    position: absolute; left: 156px; top: 261px;
    width: 236px; height: 236px; border-radius: 50%;
    background: var(--white);
    text-align: center;
  }
  .offer-amount { margin-top: 40px; font-size: 62px; line-height: 56px; font-weight: 400; color: var(--navy); }
  .offer-word { font-size: 62px; line-height: 58px; font-weight: 400; color: var(--teal); letter-spacing: 1px; }
  .offer-note { margin-top: 6px; font-size: 21px; line-height: 22px; font-weight: 500; color: var(--grey-text); }

  .brand-disc { position: absolute; border-radius: 50%; background: var(--white); }
  .card-front .brand-disc { left: 200px; top: 565px; width: 190px; height: 190px; }
  .card-back  .brand-disc { left: 17px; top: 561px; width: 216px; height: 216px; }
  .brand-name {
    position: absolute; text-align: center;
    font-weight: 600; color: var(--teal-text);
    font-size: 27px; line-height: 29px; letter-spacing: 1.5px;
  }
  .card-front .brand-name { left: 200px; top: 630px; width: 190px; }
  .card-back  .brand-name { left: 17px; top: 636px; width: 216px; }

  .front-footer {
    position: absolute; left: 0; top: 669px; width: 100%; height: 93px;
    background: var(--white);
  }
  .front-cta {
    position: absolute; left: 0; top: 722px; width: 100%;
    text-align: center; font-size: 16.5px; font-weight: 400; letter-spacing: .3px; color: var(--ink);
  }
  .front-cta strong { font-weight: 700; font-size: 17px; }

  .headline-disc {
    position: absolute; left: 41px; top: 95px;
    width: 212px; height: 212px; border-radius: 50%;
    background: var(--white);
    display: flex; align-items: center; justify-content: center;
    text-align: center; padding-top: 14px;
    font-size: 21px; line-height: 25px; font-weight: 600; color: #555; letter-spacing: .5px;
  }

  .rates-band {
    position: absolute; left: 0; top: 277px; width: 100%; height: 257px;
    background: var(--navy); color: var(--white);
  }
  .list-title { font-size: 19px; font-weight: 500; letter-spacing: .5px; }
  .prices { position: absolute; left: 33px; top: 32px; }
  .services { position: absolute; left: 337px; top: 22px; }
  .divider-v {
    position: absolute; left: 315px; top: 24px; width: 1px; height: 212px;
    background: rgba(255,255,255,.5);
  }
  .item-list { list-style: none; margin-top: 4px; }
  .prices .item-list li { font-size: 17.5px; line-height: 28.5px; font-weight: 400; }
  .services .item-list li { font-size: 16.5px; line-height: 26.2px; }
  .item-list li::before {
    content: ""; display: inline-block; width: 7px; height: 7px; border-radius: 50%;
    background: var(--teal); margin: 0 9px 2px 0; vertical-align: middle;
  }
  .prices strong { font-weight: 600; }

  .promise-band {
    position: absolute; left: 0; top: 534px; width: 100%; height: 128px;
    background: var(--teal);
  }
  .promise-list {
    position: absolute; left: 247px; top: 14px; list-style: none;
    font-family: "Open Sans", "Helvetica Neue", Arial, sans-serif;
    font-style: italic; font-weight: 800; font-size: 15.5px; line-height: 25.5px;
    color: var(--white);
  }
  .promise-list li { display: flex; align-items: center; gap: 6px; }
  .promise-list svg { width: 17px; height: 17px; flex: none; }

  .back-footer {
    position: absolute; left: 0; top: 662px; width: 100%; height: 98px;
    background: var(--white);
  }
  .contact-phone {
    position: absolute; left: 273px; top: 668px;
    font-size: 21px; font-weight: 600; color: var(--navy); letter-spacing: .5px;
  }
  .contact-email {
    position: absolute; left: 277px; top: 695px;
    font-size: 13.5px; color: var(--ink);
  }
  .divider-h {
    position: absolute; left: 25px; top: 722px; width: 504px; height: 1px; background: #999;
  }
  .address {
    position: absolute; left: 25px; top: 729px; width: 480px;
    white-space: nowrap; overflow: hidden;
    font-size: 12.5px; color: var(--ink); letter-spacing: .2px;
  }
</style>
</head>
<body>

<section class="card card-front">
  <div class="photo photo-laundry" role="img" aria-label="Hand loading a blue towel into a front-loading washing machine"></div>
  <div class="photo photo-shirts" role="img" aria-label="Folded pastel dress shirts with collars"></div>
  <div class="offer-ring"></div>
  <div class="offer">
    <div class="offer-amount">25%</div>
    <div class="offer-word">OFF</div>
    <div class="offer-note">ON YOUR<br>FIRST ORDER</div>
  </div>
  <div class="front-footer"></div>
  <div class="brand-disc"></div>
  <div class="brand-name">LORN'S<br>CLEANERS</div>
  <p class="front-cta">CALL NOW TO GET FREE PICK AND DELIVERY: <strong>614-205-3967</strong></p>
</section>

<section class="card card-back">
  <div class="photo photo-ironing" role="img" aria-label="Steam iron pressing a white shirt on an ironing board"></div>
  <div class="headline-disc">THE HIGHEST<br>QUALITY<br>CARE FOR ALL<br>YOUR VALUED<br>GARMENTS</div>

  <div class="rates-band">
    <div class="prices">
      <h2 class="list-title">PRICES</h2>
      <ul class="item-list">
        <li>Mens Business Shirts <strong>$2.00</strong></li>
        <li>Pants <strong>$4.50</strong></li>
        <li>Skirts <strong>$5.00</strong></li>
        <li>Dry Clean Shirt/Blouse <strong>$5.00</strong></li>
        <li>Dress <strong>$9.00</strong></li>
        <li>2 Piece Suits <strong>$9.00</strong></li>
      </ul>
    </div>
    <div class="divider-v"></div>
    <div class="services">
      <h2 class="list-title">SUPERIOR SERVICES</h2>
      <ul class="item-list">
        <li>Dry Cleaning</li>
        <li>Wedding Gowns</li>
        <li>Formal Wear</li>
        <li>Pressing</li>
        <li>Drapery Cleaning</li>
        <li>Bedding</li>
        <li>Wash and Fold</li>
      </ul>
    </div>
  </div>

  <div class="promise-band">
    <ul class="promise-list">
      <li><svg viewBox="0 0 20 20"><circle cx="10" cy="10" r="10" fill="#0d4a8e"/><path d="M5 10.5l3.2 3.2L15 6.8" fill="none" stroke="#fff" stroke-width="2.6" stroke-linecap="round" stroke-linejoin="round"/></svg>QUALITY CARE</li>
      <li><svg viewBox="0 0 20 20"><circle cx="10" cy="10" r="10" fill="#0d4a8e"/><path d="M5 10.5l3.2 3.2L15 6.8" fill="none" stroke="#fff" stroke-width="2.6" stroke-linecap="round" stroke-linejoin="round"/></svg>SPOTLESS GUARANTEE</li>
      <li><svg viewBox="0 0 20 20"><circle cx="10" cy="10" r="10" fill="#0d4a8e"/><path d="M5 10.5l3.2 3.2L15 6.8" fill="none" stroke="#fff" stroke-width="2.6" stroke-linecap="round" stroke-linejoin="round"/></svg>PICKUP AND DELIVERY</li>
      <li><svg viewBox="0 0 20 20"><circle cx="10" cy="10" r="10" fill="#0d4a8e"/><path d="M5 10.5l3.2 3.2L15 6.8" fill="none" stroke="#fff" stroke-width="2.6" stroke-linecap="round" stroke-linejoin="round"/></svg>RELIABLE AND AFFORDABLE</li>
    </ul>
  </div>

  <div class="back-footer"></div>
  <div class="brand-disc"></div>
  <div class="brand-name">LORN'S<br>CLEANERS</div>
  <p class="contact-phone">CALL : 614-205-3967</p>
  <p class="contact-email">email : lornscleaners@mailbox.com</p>
  <div class="divider-h"></div>
  <p class="address">ADDRESS : YOUR ADDRESS WILL BE HERE WITH DETAILS..............................................................................</p>
</section>

</body>
</html>
```